Bright Hollow Syrup labels

Design for 3" round labels for 8 oz. maple syrup jars. Must include a picture (or outline) of an irish setter, a maple leaf (?) and the name "Bright Hollow Syrup" and the location Birchwood Pond, Maine. 8 fl oz (237 ml) and Grade A Amber. Here's my shitty stab at it. I want less leaf and more dog. I've included marginal pictures of the dog. I would prefer the dog center in the middle and the leaf behind it.

```html
<!DOCTYPE html>
<html lang="en">
<head>
<meta charset="utf-8">
<title>Bright Hollow Syrup – Round Jar Labels</title>
<link href="https://fonts.googleapis.com/css2?family=Alegreya+SC:wght@800&family=Montserrat:wght@500&display=swap" rel="stylesheet">
<style>
  :root {
    --page: #ffffff;
    --cream: #f6e9d3;
    --maple-red: #b8382a;
    --label-black: #0c0c0c;
    --label-green: #1f3b2e;
    --setter-brown: #6e2a17;
    --setter-mid: #7d2e1a;
    --leaf-red: #b23a26;
  }
  html, body {
    margin: 0;
    padding: 0;
    width: 1200px;
    height: 750px;
    overflow: hidden;
    background: var(--page);
  }
  .sheet {
    position: relative;
    width: 1200px;
    height: 750px;
  }
  .label {
    position: absolute;
    top: 124px;
    width: 480px;
    height: 480px;
    filter: drop-shadow(5px 7px 6px rgba(0, 0, 0, 0.22));
  }
  .label--black { left: 114px; }
  .label--green { left: 620px; }
  .label__rim { fill: var(--cream); }
  .label--black .label__field { fill: var(--label-black); }
  .label--green .label__field { fill: var(--label-green); }
  .label__ring { fill: none; stroke: var(--cream); stroke-width: 1; }
  .brand-arc {
    font-family: "Alegreya SC", Georgia, serif;
    font-weight: 800;
    font-size: 40px;
    fill: var(--maple-red);
  }
  .location-arc {
    font-family: "Montserrat", Arial, sans-serif;
    font-weight: 500;
    font-size: 19px;
    letter-spacing: 3px;
    fill: var(--maple-red);
  }
  .spec {
    font-family: "Montserrat", Arial, sans-serif;
    font-weight: 500;
    font-size: 14px;
    fill: var(--maple-red);
  }
  .product-line {
    font-family: "Alegreya SC", Georgia, serif;
    font-weight: 800;
    fill: var(--cream);
  }
  .product-line--pure { font-size: 58px; }
  .product-line--syrup { font-size: 88px; }
</style>
</head>
<body>
<main class="sheet">

  <svg class="label label--black" viewBox="0 0 480 480" aria-label="Bright Hollow Syrup label, black">
    <defs>
      <path id="brand-path-black" d="M 77.7,196.5 A 168 168 0 0 1 402.3,196.5"/>
      <path id="location-path-black" d="M 36,240 A 204 204 0 0 0 444,240"/>
      <radialGradient id="art-black" cx="50%" cy="55%" r="55%">
        <stop offset="0%" stop-color="var(--setter-brown)"/>
        <stop offset="55%" stop-color="var(--setter-mid)"/>
        <stop offset="100%" stop-color="var(--leaf-red)"/>
      </radialGradient>
    </defs>
    <circle class="label__rim" cx="240" cy="240" r="233"/>
    <circle class="label__field" cx="240" cy="240" r="228"/>
    <circle class="label__ring" cx="240" cy="240" r="222"/>
    <ellipse role="img" aria-label="Illustration of an Irish setter in profile in front of a red maple leaf" cx="240" cy="188" rx="112" ry="92" fill="url(#art-black)"/>
    <text class="brand-arc"><textPath href="#brand-path-black" startOffset="50%" text-anchor="middle" textLength="436" lengthAdjust="spacingAndGlyphs">BRIGHT HOLLOW SYRUP</textPath></text>
    <text class="spec" x="66" y="226" text-anchor="middle">Grade A</text>
    <text class="spec" x="66" y="245" text-anchor="middle">Amber</text>
    <text class="spec" x="410" y="226" text-anchor="middle">8 FL OZ</text>
    <text class="spec" x="410" y="245" text-anchor="middle">(237 ML)</text>
    <text class="product-line product-line--pure" x="61" y="311" textLength="358" lengthAdjust="spacingAndGlyphs">PURE MAPLE</text>
    <text class="product-line product-line--syrup" x="112" y="385" textLength="256" lengthAdjust="spacingAndGlyphs">SYRUP</text>
    <text class="location-arc"><textPath href="#location-path-black" startOffset="50%" text-anchor="middle">BIRCHWOOD POND, MAINE</textPath></text>
  </svg>

  <svg class="label label--green" viewBox="0 0 480 480" aria-label="Bright Hollow Syrup label, green">
    <defs>
      <path id="brand-path-green" d="M 77.7,196.5 A 168 168 0 0 1 402.3,196.5"/>
      <path id="location-path-green" d="M 36,240 A 204 204 0 0 0 444,240"/>
      <radialGradient id="art-green" cx="50%" cy="55%" r="55%">
        <stop offset="0%" stop-color="var(--setter-brown)"/>
        <stop offset="55%" stop-color="var(--setter-mid)"/>
        <stop offset="100%" stop-color="var(--leaf-red)"/>
      </radialGradient>
    </defs>
    <circle class="label__rim" cx="240" cy="240" r="233"/>
    <circle class="label__field" cx="240" cy="240" r="228"/>
    <circle class="label__ring" cx="240" cy="240" r="222"/>
    <ellipse role="img" aria-label="Illustration of an Irish setter in profile in front of a red maple leaf" cx="240" cy="188" rx="112" ry="92" fill="url(#art-green)"/>
    <text class="brand-arc"><textPath href="#brand-path-green" startOffset="50%" text-anchor="middle" textLength="436" lengthAdjust="spacingAndGlyphs">BRIGHT HOLLOW SYRUP</textPath></text>
    <text class="spec" x="66" y="226" text-anchor="middle">Grade A</text>
    <text class="spec" x="66" y="245" text-anchor="middle">Amber</text>
    <text class="spec" x="410" y="226" text-anchor="middle">8 FL OZ</text>
    <text class="spec" x="410" y="245" text-anchor="middle">(237 ML)</text>
    <text class="product-line product-line--pure" x="61" y="311" textLength="358" lengthAdjust="spacingAndGlyphs">PURE MAPLE</text>
    <text class="product-line product-line--syrup" x="112" y="385" textLength="256" lengthAdjust="spacingAndGlyphs">SYRUP</text>
    <text class="location-arc"><textPath href="#location-path-green" startOffset="50%" text-anchor="middle">BIRCHWOOD POND, MAINE</textPath></text>
  </svg>

</main>
</body>
</html>
```